The Book Cover for "Finding the Silver Lantern of Dawn" needs redesigned

First the back ground or art work needs to be replaced or redesigned.
The title Finding the Silver Lantern of Dawn needs to be redesigned so that the words "Finding the" is diminished in size compared to the rest of the title "Silver Lantern of Dawn"
The Sub-title "Tracing the forgotten path of the Evening Wind" needs to be more pronounced and readable.
The authors name needs to be downsized.

```html
<!DOCTYPE html>
<html lang="en">
<head>
<meta charset="utf-8">
<title>Finding the Silver Lantern of Dawn — Cover</title>
<link rel="stylesheet" href="https://fonts.googleapis.com/css2?family=PT+Sans:ital,wght@0,400;0,700;1,400&family=PT+Sans+Narrow:wght@700&display=swap">
<style>
  :root {
    --page-bg: #ececec;
    --sky-top: #c9a56e;
    --sky-mid: #e9d7b4;
    --glow: #f7f1e4;
    --horizon: #dba94e;
    --ground: #0c0906;
    --title-brown: #4a2a1f;
    --ink: #1c1410;
    --author-white: #f6f2ea;
  }
  * { margin: 0; padding: 0; box-sizing: border-box; }
  html, body {
    width: 1200px;
    height: 1200px;
    overflow: hidden;
    background: var(--page-bg);
  }
  .canvas {
    width: 1200px;
    height: 1200px;
    display: flex;
    align-items: center;
    justify-content: center;
  }
  .cover {
    position: relative;
    width: 760px;
    height: 1140px;
    overflow: hidden;
    box-shadow: 0 10px 30px rgba(0,0,0,0.18);
  }
  .cover-art {
    position: absolute;
    inset: 0;
    background:
      radial-gradient(ellipse 60% 35% at 50% 58%, var(--glow) 0%, rgba(247,241,228,0) 70%),
      linear-gradient(to bottom,
        var(--sky-top) 0%,
        var(--sky-mid) 40%,
        #eedfc0 58%,
        var(--horizon) 74%,
        #c8902f 84%,
        var(--ground) 93%,
        var(--ground) 100%);
  }
  .title-block {
    position: absolute;
    top: 52px;
    left: 0;
    right: 0;
    text-align: center;
    color: var(--title-brown);
  }
  .title-lead {
    font-family: "PT Sans", sans-serif;
    font-weight: 700;
    font-size: 34px;
    letter-spacing: 0.04em;
    text-transform: uppercase;
    color: var(--ink);
  }
  .title-main {
    font-family: "PT Sans Narrow", "PT Sans", sans-serif;
    font-weight: 700;
    font-size: 168px;
    line-height: 0.86;
    text-transform: uppercase;
    margin-top: 10px;
    letter-spacing: 0.005em;
  }
  .title-main span { display: block; }
  .subtitle {
    position: absolute;
    top: 620px;
    left: 60px;
    right: 60px;
    text-align: center;
    font-family: "PT Sans", sans-serif;
    font-weight: 700;
    font-size: 38px;
    line-height: 1.2;
    color: var(--ink);
  }
  .author {
    position: absolute;
    bottom: 44px;
    left: 0;
    right: 0;
    text-align: center;
    font-family: "PT Sans", sans-serif;
    font-weight: 700;
    font-size: 28px;
    letter-spacing: 0.06em;
    text-transform: uppercase;
    color: var(--author-white);
  }
</style>
</head>
<body>
  <main class="canvas">
    <article class="cover">
      <div class="cover-art" role="img" aria-label="Golden sunset over the sea with the silhouette of a woman lifting a joyful child, dark grass along the bottom"></div>
      <header class="title-block">
        <p class="title-lead">Finding the</p>
        <h1 class="title-main">
          <span>Silver</span>
          <span>Lantern</span>
          <span>of Dawn</span>
        </h1>
      </header>
      <p class="subtitle">Tracing the forgotten path of the Evening Wind</p>
      <p class="author">RJ Alder Whitcombe</p>
    </article>
  </main>
</body>
</html>
```